Borvelux Bootcamp Schedule

Nothing complicated just a basic (but well designed) bootcamp schedule in the form of a flyer to hand out.

Explanation below:

We hand out our fitness bootcamp schedule to potential clients and members on a regular basis and want to make a good impression about who we are and the detail we put into our material and services. I've attached a current schedule that we send out. I'm hoping we can get this as a PSD file so we can change the times and days as needed as our company grows. I've also attached a jpeg of our new website design and what that will look like along with our Borvelux Personal Training Studio logo and our Borvelux Bootcamps logo. The schedule is for our bootcamp. I also included several photos of our facility and if you want pictures of anything up close or anything that you would want in the design I can snap a good photo and send it. I included an attempt of my own to make a schedule that I wasn't too fond of but tried :)

Industry/Entity Type

Fitness

```html
<!DOCTYPE html>
<html lang="en">
<head>
<meta charset="utf-8">
<title>Borvelux Bootcamps – Fitness Boot Camp Schedule</title>
<link href="https://fonts.googleapis.com/css2?family=Black+Ops+One&family=Roboto+Condensed:ital,wght@0,400;0,700;1,700&display=swap" rel="stylesheet">
<style>
  :root {
    --orange: #c96a24;
    --orange-dark: #8f4514;
    --ink: #2b2b2b;
    --header: #3c3c3c;
    --row: #e2e2e2;
    --row-alt: #d9d9d9;
    --rule: #f4f4f4;
    --white: #ffffff;
    --concrete-light: #bdbdbb;
    --concrete-dark: #8d8d8b;
    --turf: #2e8a3a;
    --wall: #4b4e53;
  }
  * { box-sizing: border-box; margin: 0; padding: 0; }
  html, body { width: 945px; height: 1200px; overflow: hidden; background: var(--white); }
  .flyer { position: relative; width: 945px; height: 1200px; overflow: hidden; font-family: "Roboto Condensed", "Arial Narrow", sans-serif; }

  .facility-photo {
    position: absolute; left: 0; top: 0; width: 945px; height: 567px;
    background:
      linear-gradient(90deg, rgba(214,110,40,0.55) 0%, rgba(214,110,40,0) 7%),
      radial-gradient(ellipse 60% 45% at 45% 62%, rgba(70,70,78,0.55) 0%, rgba(70,70,78,0) 100%),
      linear-gradient(180deg, #55585d 0%, #5e6166 22%, #4a5a4c 40%, #33863e 55%, var(--turf) 80%, #2a7d35 100%);
  }
  .concrete {
    position: absolute; left: 0; top: 567px; width: 945px; height: 633px;
    background: radial-gradient(ellipse at 50% 40%, var(--concrete-light) 0%, #a8a8a6 55%, var(--concrete-dark) 100%);
  }

  .brand-name {
    position: absolute; left: 224px; top: 108px; width: 514px;
    font-weight: 700; font-size: 60px; line-height: 64px;
    color: var(--white); text-align: center; letter-spacing: 2px;
  }

  .title-ribbon { position: absolute; left: 128px; top: 474px; width: 712px; height: 180px; }
  .title-text {
    position: absolute; left: 177px; top: 512px; width: 610px;
    font-family: "Black Ops One", sans-serif; font-size: 42px; line-height: 50px;
    color: var(--white); text-align: center; letter-spacing: 1px;
  }

  .schedule {
    position: absolute; left: 47px; top: 712px; width: 856px;
    border-collapse: collapse; font-size: 26px; color: var(--ink);
  }
  .schedule th {
    background: var(--header); color: var(--white); font-weight: 700;
    height: 49px; text-align: center; border: 2px solid var(--rule);
  }
  .schedule td {
    height: 43px; background: var(--row); border: 2px solid var(--rule);
    padding: 0 12px 0 26px; white-space: nowrap;
  }
  .schedule tr:nth-child(even) td { background: var(--row-alt); }
  .schedule .col-day { width: 168px; padding-left: 26px; }
  .schedule .col-am { width: 342px; }
  .schedule .closed { float: right; font-weight: 700; }

  .length-note { position: absolute; left: 92px; top: 1098px; width: 764px; height: 54px; }
  .length-text {
    position: absolute; left: 92px; top: 1098px; width: 764px; line-height: 54px;
    text-align: center; font-weight: 700; font-style: italic; font-size: 33px; color: var(--orange);
  }
</style>
</head>
<body>
<main class="flyer">
  <div class="facility-photo" role="img" aria-label="Photo of two people doing floor exercises on green turf inside the training studio"></div>
  <div class="concrete" role="img" aria-label="Grey concrete texture background with orange hazard stripes"></div>

  <p class="brand-name">BORVELUX<br>BOOTCAMPS</p>

  <svg class="title-ribbon" viewBox="0 0 712 180" aria-hidden="true">
    <polygon points="0,10 60,10 60,150 22,150 34,80" fill="var(--orange-dark)"/>
    <polygon points="712,10 652,10 652,150 690,150 678,80" fill="var(--orange-dark)"/>
    <polygon points="49,18 663,8 663,164 49,172" fill="var(--ink)" fill-opacity="0.45"/>
    <polygon points="44,14 658,4 658,158 44,166" fill="var(--orange)"/>
  </svg>
  <h1 class="title-text">FITNESS BOOT CAMP<br>SCHEDULE</h1>

  <table class="schedule">
    <thead>
      <tr><th class="col-day">Days</th><th class="col-am">Timings (AM)</th><th>Timings (PM)</th></tr>
    </thead>
    <tbody>
      <tr><td class="col-day">Monday</td><td>6am, 8:30am, 12.00 noon,</td><td>4:30pm, 5:30pm, 6:30pm</td></tr>
      <tr><td class="col-day">Tuesday</td><td>6am, 8:30am, 12.00 noon,</td><td>4:30pm, 5:30pm, 6:30pm</td></tr>
      <tr><td class="col-day">Wednesday</td><td>6am, 8:30am, 12.00 noon,</td><td>4:30pm, 5:30pm, 6:30pm</td></tr>
      <tr><td class="col-day">Thursday</td><td>6am, 8:30am, 12.00 noon,</td><td>4:30pm, 5:30pm, 6:30pm</td></tr>
      <tr><td class="col-day">Friday</td><td>6am, 8:30am, 12.00 noon,</td><td>4:30pm, 5:30pm, 6:30pm</td></tr>
      <tr><td class="col-day">Saturday</td><td>9am.</td><td></td></tr>
      <tr><td class="col-day" colspan="2">Sunday / Major Holidays <span class="closed">Closed</span></td><td></td></tr>
    </tbody>
  </table>

  <svg class="length-note" viewBox="0 0 764 54" aria-hidden="true">
    <polygon points="0,0 764,0 744,54 20,54" fill="var(--ink)"/>
  </svg>
  <p class="length-text">*All Boot Camps are 50 minutes in length</p>
</main>
</body>
</html>
```